Harbinvale Crest Inc Tank Lining Services

I would check out our website for an a quick understanding of what Blasting and Painting "is". www.harbinvalecrestinc.example

I need to Design "sales postcard" or "company postcard" that outlines the TANK LINING division of our company. (What is a "tank lining"? It is a coating applied to the interior of a Water Tank or "Water Tower". There are certifications and special equipment needed to provide these services that make it a unique market) This is a NEW service we are offing to our customers.

We want to include photo's of: Sand Blasting, Painting, and Welding on a Ground Storage Tank. (please see attached)

Bullet points to include:
-Critical Areas
-Tank Inspections
-Manway Installation
-Fire/Domestic Water

Please Note: a little says a lot in regards to regards to data crammed into "postcards". Our market is one that won't need to be "spoon" fed. I need potential clients to read the name and our contact info (obviously).

Target Market(s)

Building Owners

Industry/Entity Type

Construction

Font styles to use
Sans Serif

Colors
0054AA
0677BA
7BADD7
CADEEF
E8F1F8

Requirements
Must have
• Layered photos or pictures
Nice to have
• Cropped Layered photos are good
Should not have
• to much clutter

```html
<!DOCTYPE html>
<html lang="en">
<head>
<meta charset="utf-8">
<title>Harbinvale Crest Inc — Tank Lining Postcard</title>
<link rel="stylesheet" href="https://fonts.googleapis.com/css2?family=Montserrat:wght@400;500;600;700;800&display=swap">
<style>
  :root {
    --blue-deep: #0054AA;
    --blue: #0677BA;
    --blue-soft: #7BADD7;
    --blue-pale: #CADEEF;
    --blue-mist: #E8F1F8;
    --charcoal: #3a3a3c;
    --grey: #8e8e90;
    --ink: #2b2b2d;
    --paper: #f7f7f7;
    --yellow: #f2d23a;
    --stage: #8a8a8a;
  }
  * { box-sizing: border-box; margin: 0; padding: 0; }
  html, body { width: 1200px; height: 900px; overflow: hidden; }
  body {
    background: var(--stage);
    font-family: "Montserrat", sans-serif;
    color: var(--ink);
    position: relative;
  }

  /* ---------- shared ---------- */
  .postcard { position: absolute; width: 566px; height: 400px; box-shadow: 0 8px 22px rgba(0,0,0,.28); }
  .photo { position: absolute; border: 4px solid #fff; }
  .brand { display: flex; align-items: center; gap: 7px; }
  .brand-square { width: 20px; height: 20px; background: var(--blue-deep); flex: none; }
  .brand-name { font-weight: 700; font-size: 15px; color: #4a4a4c; letter-spacing: -.2px; }
  .info-bar { position: absolute; background: var(--charcoal); color: #fff; display: flex; align-items: center; }

  /* ---------- front ---------- */
  .postcard-front { left: 20px; top: 250px; background: var(--blue-deep); padding: 0 0 10px 10px; }
  .front-panel { position: relative; width: 100%; height: 100%; background: var(--paper); overflow: hidden; }
  .front-panel .brand { position: absolute; left: 14px; top: 16px; }
  .tagline-banner {
    position: absolute; left: 14px; top: 48px; width: 190px;
    background: var(--grey); color: #fff; font-weight: 800; font-size: 12.5px;
    line-height: 1.2; padding: 6px 9px; text-transform: uppercase;
  }
  .lining-question { position: absolute; left: 14px; top: 100px; font-size: 11px; font-weight: 700; color: var(--blue-deep); }
  .lining-answer { position: absolute; left: 14px; top: 116px; width: 188px; font-size: 7.6px; line-height: 1.4; color: #444; }
  .service-list { position: absolute; left: 14px; top: 196px; list-style: none; }
  .service-list li { display: flex; align-items: center; gap: 8px; height: 34px; font-size: 12px; font-weight: 600; color: var(--ink); white-space: nowrap; }
  .service-icon { width: 28px; height: 28px; border-radius: 50%; background: var(--blue-deep); box-shadow: 0 0 0 2px var(--blue-pale); display: flex; align-items: center; justify-content: center; flex: none; }
  .front-panel .info-bar { left: 60px; top: 342px; width: 296px; height: 26px; padding-left: 16px; font-size: 11.5px; font-weight: 600; letter-spacing: .3px; }
  .photo-coating { left: 206px; top: 12px; width: 150px; height: 322px; background: linear-gradient(160deg, #5a5048 0%, #c9c6c0 45%, #3b3530 100%); }
  .photo-welding { left: 362px; top: 12px; width: 174px; height: 150px; background: linear-gradient(135deg, #2d3a52 0%, #b8263a 50%, #e8c43a 100%); }
  .photo-blasting { left: 362px; top: 166px; width: 174px; height: 202px; background: linear-gradient(150deg, #a5a190 0%, #5e6a5c 50%, #2e3428 100%); }

  /* ---------- back ---------- */
  .postcard-back { left: 614px; top: 250px; background: var(--paper); }
  .back-content {
    position: absolute; left: 0; top: 0; width: 312px; height: 400px;
    border-left: 8px solid var(--blue-deep); border-bottom: 8px solid var(--blue-deep);
    border-right: 5px solid var(--blue-deep); padding: 14px 12px 0 12px;
  }
  .section-title { font-size: 12px; font-weight: 800; color: var(--blue-deep); text-transform: uppercase; }
  .about-text { font-size: 7.4px; line-height: 1.45; color: #444; margin-top: 3px; }
  .back-photos { display: flex; gap: 8px; margin-top: 8px; height: 78px; }
  .back-photos div { flex: 1; }
  .photo-spraying { background: linear-gradient(140deg, #e6e9ec 0%, #b8c1c9 60%, #2b5aa0 100%); }
  .photo-shop { background: linear-gradient(140deg, #9aa0a6 0%, #d7d9db 50%, #6e6a66 100%); }
  .check-columns { display: grid; grid-template-columns: 1fr 1fr; column-gap: 10px; margin-top: 3px; }
  .check-list { list-style: none; }
  .check-list li { display: flex; align-items: center; gap: 5px; font-size: 9px; font-weight: 500; line-height: 1.55; color: var(--ink); }
  .tick { width: 9px; height: 9px; border-radius: 50%; background: #9a9a9c; display: flex; align-items: center; justify-content: center; flex: none; }
  .back-block { margin-top: 8px; }
  .back-content .info-bar { left: 0; right: 0; bottom: 0; height: 26px; padding: 0 10px; gap: 14px; font-size: 9px; font-weight: 500; }
  .contact-item { display: flex; align-items: center; gap: 5px; }
  .contact-icon { width: 15px; height: 15px; border-radius: 50%; border: 1px solid #bbb; display: flex; align-items: center; justify-content: center; }

  .mailing-side { position: absolute; left: 312px; top: 0; width: 254px; height: 400px; }
  .stamp-box { position: absolute; right: 16px; top: 16px; width: 66px; height: 58px; background: #e2e2e2; }
  .mailing-side .brand { position: absolute; left: 18px; top: 90px; }
  .return-address { position: absolute; left: 18px; top: 118px; font-size: 8.5px; line-height: 1.4; color: #444; }
  .address-lines { position: absolute; left: 40px; right: 18px; top: 170px; }
  .address-lines span { display: block; height: 1px; background: #cfcfcf; margin-bottom: 32px; }
  .mailing-web { position: absolute; right: 16px; bottom: 24px; font-size: 9.5px; font-weight: 600; color: var(--ink); }
  .yellow-edge { position: absolute; left: 0; right: 0; bottom: 0; height: 7px; background: var(--yellow); }
</style>
</head>
<body>

  <!-- Front of postcard -->
  <section class="postcard postcard-front">
    <div class="front-panel">
      <div class="brand">
        <span class="brand-square"></span>
        <span class="brand-name">Harbinvale Crest</span>
      </div>

      <div class="tagline-banner">Precise, Professional, Protected</div>

      <h2 class="lining-question">What is a "tank lining"?</h2>
      <p class="lining-answer">It is a coating applied to the interior of a Water Tank or "Water Tower". There are certifications and special equipment needed to provide these services that make it a unique market. This is a NEW service we are offering to our customers.</p>

      <ul class="service-list">
        <li>
          <span class="service-icon">
            <svg width="14" height="14" viewBox="0 0 14 14" fill="none" stroke="#fff" stroke-width="1.3"><rect x="2" y="2" width="10" height="10"/><path d="M2 7h10M7 2v10"/></svg>
          </span>Critical Areas
        </li>
        <li>
          <span class="service-icon">
            <svg width="14" height="14" viewBox="0 0 14 14" fill="none" stroke="#fff" stroke-width="1.4"><circle cx="6" cy="6" r="4"/><path d="M9 9l3.5 3.5"/></svg>
          </span>Tank Inspections
        </li>
        <li>
          <span class="service-icon">
            <svg width="14" height="14" viewBox="0 0 14 14" fill="none" stroke="#fff" stroke-width="1.2"><circle cx="7" cy="7" r="5.5"/><path d="M3 5h8M2.5 7h9M3 9h8"/></svg>
          </span>Manway Installation
        </li>
        <li>
          <span class="service-icon">
            <svg width="14" height="14" viewBox="0 0 14 14" fill="#fff"><path d="M7 1c1 3 4 4.5 4 8a4 4 0 0 1-8 0c0-2 1-3 2-4 0 1.5.6 2.3 1.4 2.6C6 5.5 6.5 3 7 1z"/></svg>
          </span>Fire/Domestic Water
        </li>
      </ul>

      <div class="photo photo-coating" role="img" aria-label="Worker in protective suit and respirator spraying a lining inside a tank"></div>
      <div class="photo photo-welding" role="img" aria-label="Welder working on a red ground storage tank wall"></div>
      <div class="photo photo-blasting" role="img" aria-label="Worker inside a water tank with a work light after blasting"></div>

      <div class="info-bar">www.harbinvalecrestinc.example</div>
    </div>
  </section>

  <!-- Back of postcard -->
  <section class="postcard postcard-back">
    <div class="back-content">
      <h2 class="section-title">About Us</h2>
      <p class="about-text">At Harbinvale Crest Inc., we have only one purpose – satisfying you and your needs for protective coating services. Today, we are proud to be the supplier of choice for many of the world's leading energy companies, oil and gas firms, and petrochemical concerns…however, every customer gets our full attention when it comes to protecting their critical equipment.</p>

      <div class="back-photos">
        <div class="photo-spraying" role="img" aria-label="Painter in white coveralls spray coating a surface"></div>
        <div class="photo-shop" role="img" aria-label="Abrasive blasting inside a fabrication shop"></div>
      </div>

      <div class="back-block">
        <h3 class="section-title">Industries We Serve:</h3>
        <div class="check-columns">
          <ul class="check-list">
            <li><span class="tick"><svg width="6" height="6" viewBox="0 0 6 6" fill="none" stroke="#fff" stroke-width="1.2"><path d="M1 3l1.3 1.3L5 1.6"/></svg></span>Structural Steel</li>
            <li><span class="tick"><svg width="6" height="6" viewBox="0 0 6 6" fill="none" stroke="#fff" stroke-width="1.2"><path d="M1 3l1.3 1.3L5 1.6"/></svg></span>Subsea Structures</li>
            <li><span class="tick"><svg width="6" height="6" viewBox="0 0 6 6" fill="none" stroke="#fff" stroke-width="1.2"><path d="M1 3l1.3 1.3L5 1.6"/></svg></span>Assemblies</li>
            <li><span class="tick"><svg width="6" height="6" viewBox="0 0 6 6" fill="none" stroke="#fff" stroke-width="1.2"><path d="M1 3l1.3 1.3L5 1.6"/></svg></span>Skid Packages</li>
          </ul>
          <ul class="check-list">
            <li><span class="tick"><svg width="6" height="6" viewBox="0 0 6 6" fill="none" stroke="#fff" stroke-width="1.2"><path d="M1 3l1.3 1.3L5 1.6"/></svg></span>Inhouse and Field Service</li>
            <li><span class="tick"><svg width="6" height="6" viewBox="0 0 6 6" fill="none" stroke="#fff" stroke-width="1.2"><path d="M1 3l1.3 1.3L5 1.6"/></svg></span>Waste Management</li>
            <li><span class="tick"><svg width="6" height="6" viewBox="0 0 6 6" fill="none" stroke="#fff" stroke-width="1.2"><path d="M1 3l1.3 1.3L5 1.6"/></svg></span>Heavy Equipment</li>
          </ul>
        </div>
      </div>

      <div class="back-block">
        <h3 class="section-title">Our Services:</h3>
        <div class="check-columns">
          <ul class="check-list">
            <li><span class="tick"><svg width="6" height="6" viewBox="0 0 6 6" fill="none" stroke="#fff" stroke-width="1.2"><path d="M1 3l1.3 1.3L5 1.6"/></svg></span>Abrasive Blasting</li>
            <li><span class="tick"><svg width="6" height="6" viewBox="0 0 6 6" fill="none" stroke="#fff" stroke-width="1.2"><path d="M1 3l1.3 1.3L5 1.6"/></svg></span>Coating Application</li>
            <li><span class="tick"><svg width="6" height="6" viewBox="0 0 6 6" fill="none" stroke="#fff" stroke-width="1.2"><path d="M1 3l1.3 1.3L5 1.6"/></svg></span>Coating Inspection</li>
          </ul>
          <ul class="check-list">
            <li><span class="tick"><svg width="6" height="6" viewBox="0 0 6 6" fill="none" stroke="#fff" stroke-width="1.2"><path d="M1 3l1.3 1.3L5 1.6"/></svg></span>Fire Proofing</li>
            <li><span class="tick"><svg width="6" height="6" viewBox="0 0 6 6" fill="none" stroke="#fff" stroke-width="1.2"><path d="M1 3l1.3 1.3L5 1.6"/></svg></span>Field Services</li>
            <li><span class="tick"><svg width="6" height="6" viewBox="0 0 6 6" fill="none" stroke="#fff" stroke-width="1.2"><path d="M1 3l1.3 1.3L5 1.6"/></svg></span>Heavy Lifting Capacity</li>
          </ul>
        </div>
      </div>

      <div class="info-bar">
        <span class="contact-item">
          <span class="contact-icon"><svg width="8" height="8" viewBox="0 0 8 8" fill="#fff"><path d="M1.5 .5l1.4 1.6-.7 1a4 4 0 0 0 1.7 1.7l1-.7 1.6 1.4-.8 1.2C3.5 6.6 1.4 4.5.3 1.3z"/></svg></span>
          (555) 014-2290
        </span>
        <span class="contact-item">
          <span class="contact-icon"><svg width="8" height="7" viewBox="0 0 8 7" fill="none" stroke="#fff" stroke-width=".9"><rect x=".5" y=".5" width="7" height="6"/><path d="M.5 .5L4 3.8 7.5 .5"/></svg></span>
          quotes@harbinvalecrestinc.example
        </span>
      </div>
    </div>

    <div class="mailing-side">
      <div class="stamp-box"></div>
      <div class="brand">
        <span class="brand-square"></span>
        <span class="brand-name">Harbinvale Crest</span>
      </div>
      <p class="return-address">2280 Larkmoor Ln.<br>Fenwick, Texas 77990</p>
      <div class="address-lines"><span></span><span></span><span></span><span></span></div>
      <p class="mailing-web">www.harbinvalecrestinc.example</p>
      <div class="yellow-edge"></div>
    </div>
  </section>

</body>
</html>
```